依頼詳細
<サイトマップ>
①TOPページ
②SALON(店舗情報)
③STAFF(スタッフ紹介)
④STYLE(ギャラリー)
⑤COUPON(クーポン)
⑥FEATURE(当店の特徴)
⑦RECRUIT/COMPANY(求人・会社概要)
⑧BLOG(サイト内ブログ)
⑨NEWS(サイト内ブログ)
⑩MENU(メニュー)
⑪VOICE(お客様の声)
⑫GUEST SNAP(ゲストスナップ)

<デザインテイスト>
・ナチュラル  ・優しい  ・モダン  ・清潔な

<顧客ターゲット>
・女性
・20代~50代
①40代 ②50代 ③20代
・学生、会社員、自営業、未婚、既婚、妊婦、子育て、中年

【競合サイト】
http://www.tintomopalor.j(大阪中心のカラー専門サロン)
http://www.brisk-lumen.j(大きいサロン)
http://www.vexo-rud.co (北海道で大きいサロン)

【要望】
・pinquorのアイコンをサイト内に配置してください。
・予約が外部のためバナーなどを配置して頂けると嬉しいです。
・「VOICE」ページにはA4サイズのカウンセリングシートなどを
お客様に記入していただいたものを添付する予定ですので、TOpに
新着エリアなどがあってもうれしいです。
・ブログ、新着は新着BOXで配置して頂きたいです。

※素材は追記分内に書いています。
水色系
【素材】
■ミルカノ
素材として定期ダウンロードできる画像は使用して頂いて構いません。
その際にカンプ画像でダウンロードしてください。
(画像検索した際に出てくるサムネール下の画像番号の横にミルカノのマーク
があるものは使用不可できません・・・)
その他の素材に関しては、フリーで提供可能なものでお願いします。
■サロン外観・内装写真(ロゴ入り)
http://quolbank.jp/download/e3f7c2a9d81b04f65e2c7a93d0b1f48e27cd5a16
ダウンロードパスワード ruqwept4

すみません、ミルカノのURL添付し忘れてました。
https://jp.mirkano.com/

宜しくお願いします。
今回、当サロンのコンペに閲覧・ご提案して頂きましたデザイナー様
誠にありがとうございます!!
今でもたくさんのデザイン案を提案して頂いておりますが、もう少し色々なデザイン案を見たいという事もあり、1週間コンペ期間を延長することと致しました。
依頼詳細に囚われず、色みやレイアウトもデザイナー様の自由にデザインして頂いたものをみたいので是非、提案頂ければとても嬉しいです!!
(できれば、入れて頂くページは変えないでほしいです。)
どうぞ、宜しくお願い致します。

シンプルな中にも細部までの細やかなデザインや、デザイナー様のセンスの良さもあってサロンにとてもあったデザインに仕上がっていると思います。
とても満足しています。

今回ご提案していただいたデザイナー様へ
たくさんのデザイン案を度提案頂きまして、誠にありがとうございました。
”カラー専門店”という少し珍しい業態で当サロンの良さをうまく取り入れてくださっている方が多い中で一つに絞るのが中々、大変ではありました。
どれももったいないデザインばかりでした。。。
またこのような機会がございましたら是非ご提案していただければ幸いでございます。
ありがとうございました。

```html
<!DOCTYPE html>
<html lang="ja">
<head>
<meta charset="utf-8">
<title>Sorana | ヘアカラー専門サロン</title>
<link rel="stylesheet" href="https://fonts.googleapis.com/css2?family=Noto+Sans+JP:wght@400;500;700&family=Cormorant+Garamond:wght@500;600&display=swap">
<style>
:root{
  --sky:#7cc2ea;
  --sky-deep:#4fa6dc;
  --blue:#5f93ef;
  --blue-soft:#a9c7f5;
  --blue-pale:#d9e8fb;
  --mist:#eaf1f7;
  --ink:#4a5560;
  --ink-soft:#7a8590;
  --white:#ffffff;
  --line:#9fd0ee;
}
*{margin:0;padding:0;box-sizing:border-box}
html,body{width:1200px;height:2312px;overflow:hidden}
body{position:relative;background:var(--white);font-family:"Noto Sans JP",sans-serif;color:var(--ink)}
.abs{position:absolute}

.site-header{left:0;top:0;width:1200px;height:48px;background:var(--sky);display:flex;align-items:center;padding:0 28px}
.brand{display:flex;align-items:center;gap:8px;color:var(--white);font-size:15px;font-weight:500;letter-spacing:.06em}
.brand-dot{width:26px;height:26px;border-radius:50%;border:2px solid var(--white)}
.global-nav{position:absolute;left:270px;top:0;height:48px;display:flex;gap:26px;align-items:center}
.global-nav a{color:var(--white);font-size:12px;text-decoration:none;letter-spacing:.08em}
.social{position:absolute;right:260px;top:14px;display:flex;align-items:center;gap:6px;color:var(--white);font-size:11px}
.social span.dot{width:20px;height:20px;border-radius:50%;background:var(--white)}

.hero{left:0;top:48px;width:1200px;height:512px;background:#eef3f6}
.hero-visual{position:absolute;left:96px;top:12px;width:1008px;height:482px;border-radius:10px;background:linear-gradient(100deg,#d9cfc4 0%,#efe8df 35%,#f7f5f1 60%,#ffffff 100%)}
.hero-copy{position:absolute;left:560px;top:222px;color:#5b6a5a}
.hero-lead{font-size:16px;letter-spacing:.05em;margin-left:96px}
.hero-row{display:flex;align-items:center;gap:22px;margin-top:14px}
.hero-mark{width:84px;height:84px;border-radius:50%;background:var(--white);border:2px solid #a9c98e;display:flex;align-items:center;justify-content:center;font-size:16px;font-weight:500;color:#6c9d54}
.hero-date{font-family:"Cormorant Garamond",serif;font-size:30px;font-weight:600;color:#5a6a60}
.hero-date small{font-size:16px}
.hero-title{font-family:"Cormorant Garamond",serif;font-size:62px;font-weight:600;color:#55655a;letter-spacing:.04em;line-height:1}
.arrow{position:absolute;top:270px;width:36px;height:36px;border-radius:50%;background:#4d5358}
.arrow svg{display:block}
.arrow.prev{left:84px}.arrow.next{right:84px}

.thumbs{left:320px;top:588px;display:flex;gap:6px}
.thumb{width:75px;height:78px;position:relative}
.thumb span{position:absolute;left:0;right:0;top:30px;text-align:center;color:var(--white);font-weight:700;font-size:14px;letter-spacing:.1em}

.news{left:0;top:720px;width:1200px;height:370px;background:var(--mist)}
.news h2{text-align:center;color:var(--sky-deep);font-size:17px;font-weight:500;letter-spacing:.12em;margin-top:28px}
.news h2::after{content:"";display:block;width:40px;height:2px;background:var(--sky-deep);margin:8px auto 0}
.news-list{width:760px;margin:22px auto 0;background:var(--white);list-style:none}
.news-list li{display:flex;height:56px;align-items:center;border-bottom:1px solid #dbe6ee;padding-left:50px;font-size:13px}
.news-list time{width:190px;color:var(--sky-deep);font-weight:700}
.news-more{display:block;width:120px;height:30px;margin:28px auto 0;border:1px solid #b9cbd8;background:var(--white);text-align:center;line-height:28px;font-size:11px;color:var(--ink-soft);letter-spacing:.1em}

.menu-circle{width:236px;height:236px;border-radius:50%;display:flex;flex-direction:column;align-items:center;justify-content:center;text-align:center}
.menu-circle b{font-size:20px;font-weight:700;letter-spacing:.08em}
.menu-circle small{font-size:11px;margin-top:6px}
.c-outline{background:var(--white);border:5px solid var(--blue-soft);color:var(--blue)}
.c-solid{background:var(--blue);color:var(--white)}
.c-soft{background:var(--blue-soft);color:var(--white)}
.c-pale{background:var(--blue-pale);color:var(--blue)}
.photo-circle{width:236px;height:236px;border-radius:50%}

.message{left:100px;top:1760px;width:1000px;height:280px;border:2px solid var(--line);background:var(--white)}
.message-photo{position:absolute;left:12px;top:12px;width:330px;height:252px;background:linear-gradient(120deg,#cfd8de,#eef0ef 55%,#e4d9cf)}
.message-body{position:absolute;left:380px;top:34px;width:580px}
.message-body h3{font-size:19px;font-weight:500;line-height:1.6;color:var(--ink)}
.message-body .lead{font-size:12px;margin:8px 0 12px;color:var(--ink-soft)}
.message-body p{font-size:12px;line-height:1.9;color:var(--ink-soft)}

.site-footer{left:0;top:2080px;width:1200px;height:232px;background:var(--sky-deep);color:var(--white)}
.foot-col{position:absolute;top:34px;list-style:none;font-size:11px;line-height:2.1}
.foot-address{position:absolute;left:880px;top:34px;font-size:11px;line-height:2}
.copyright{position:absolute;right:100px;bottom:16px;font-size:10px}
</style>
</head>
<body>

<header class="site-header abs">
  <div class="brand"><span class="brand-dot"></span>Sorana</div>
  <nav class="global-nav">
    <a>TOP</a><a>SALON</a><a>MENU</a><a>NEWS</a><a>STAFF</a><a>STYLE</a><a>VOICE</a><a>RECRUIT</a>
  </nav>
  <div class="social"><span class="dot"></span>pinquor</div>
</header>

<section class="hero abs">
  <div class="hero-visual" role="img" aria-label="明るいサロンでヘアカラーを楽しむ女性の写真"></div>
  <div class="hero-copy">
    <p class="hero-lead">ヘアカラーを得意とした、新感覚サロン「ソラナ」</p>
    <div class="hero-row">
      <div class="hero-mark">Sorana</div>
      <div>
        <div class="hero-date">2015.2.20 <small>fri</small></div>
        <div class="hero-title">GRAND OPEN</div>
      </div>
    </div>
  </div>
  <div class="arrow prev"><svg width="36" height="36"><path d="M21 11l-7 7 7 7" fill="none" stroke="#fff" stroke-width="2.5"/></svg></div>
  <div class="arrow next"><svg width="36" height="36"><path d="M15 11l7 7-7 7" fill="none" stroke="#fff" stroke-width="2.5"/></svg></div>
</section>

<div class="thumbs abs">
  <div class="thumb" role="img" aria-label="サロン内装の写真" style="background:linear-gradient(#e9e2d8,#cfc3b4)"></div>
  <div class="thumb" role="img" aria-label="カラーリング中の写真" style="background:linear-gradient(#f0d9c4,#d8b394)"></div>
  <div class="thumb" role="img" aria-label="女性スタッフの写真" style="background:linear-gradient(#f3ede6,#dccdbd)"></div>
  <div class="thumb" role="img" aria-label="ブログ用の写真" style="background:linear-gradient(#bfc8d4,#8e9bab)"><span>BLOG</span></div>
  <div class="thumb" role="img" aria-label="ヘアスタイルの写真" style="background:linear-gradient(#e8d8c6,#c79f7c)"></div>
  <div class="thumb" role="img" aria-label="笑顔の女性客の写真" style="background:linear-gradient(#f4efe9,#ddd0c2)"></div>
  <div class="thumb" role="img" aria-label="カラーサンプルの写真" style="background:linear-gradient(#e3d2c2,#b89375)"></div>
</div>

<section class="news abs">
  <h2>NEWS</h2>
  <ul class="news-list">
    <li><time>2015.02.01</time>ここにテキストが入ります。ここにテキストが入ります。</li>
    <li><time>2015.01.20</time>ここにテキストが入ります。ここにテキストが入ります。</li>
    <li><time>2015.01.10</time>ここにテキストが入ります。ここにテキストが入ります。</li>
  </ul>
  <a class="news-more">MORE</a>
</section>

<a class="menu-circle c-outline abs" style="left:128px;top:1120px"><b>MENU</b><small>メニュー・料金</small></a>
<a class="menu-circle c-soft abs" style="left:380px;top:1120px"><b>STYLE</b><small>ギャラリー</small></a>
<a class="menu-circle c-pale abs" style="left:632px;top:1120px"><b>SALON</b><small>店舗情報</small></a>
<div class="photo-circle abs" role="img" aria-label="サロン外観の写真" style="left:884px;top:1120px;background:linear-gradient(135deg,#6d6a66,#b9b4ad 60%,#e2ddd6)"></div>

<a class="menu-circle c-solid abs" style="left:128px;top:1380px"><b>COUPON</b><small>クーポン</small></a>
<div class="photo-circle abs" role="img" aria-label="カラーリングした髪の写真" style="left:380px;top:1380px;background:linear-gradient(135deg,#8a6b55,#c9a58a 55%,#e9dccd)"></div>
<a class="menu-circle c-outline abs" style="left:632px;top:1380px"><b>GUESTSNAP</b><small>ゲストスナップ</small></a>
<a class="menu-circle c-solid abs" style="left:884px;top:1380px"><b>RECRUIT/<br>COMPANY</b></a>

<section class="message abs">
  <div class="message-photo" role="img" aria-label="リラックスして微笑む女性客の写真"></div>
  <div class="message-body">
    <h3>「忙しくて美容院に行く時間がない・・・」<br>「薬剤で傷んで、髪が自然に伸ばせない・・・」</h3>
    <p class="lead">そんなお客様の悩みにお応えします。</p>
    <p>ここにテキストが入ります。ここにテキストが入ります。ここにテキストが入ります。<br>ここにテキストが入ります。ここにテキストが入ります。ここにテキストが入ります。<br>ここにテキストが入ります。ここにテキストが入ります。</p>
  </div>
</section>

<footer class="site-footer abs">
  <ul class="foot-col" style="left:100px"><li>＞TOP</li><li>＞SALON<br>（店舗情報）</li><li>＞STAFF</li><li>＞STYLE<br>（ギャラリー）</li></ul>
  <ul class="foot-col" style="left:300px"><li>＞COUPON</li><li>＞FEATURE<br>（当店の特徴）</li><li>＞RECRUIT/COMPANY<br>（求人・会社概要）</li><li>＞BLOG</li></ul>
  <ul class="foot-col" style="left:520px"><li>＞NEWS</li><li>＞MENU</li><li>＞VOICE<br>（お客様の声）</li><li>＞GUEST SNAP<br>（ゲストスナップ）</li></ul>
  <div class="foot-address">〒000-0000<br>空見市青葉町1-2-3<br>【営業時間】10:00〜20:00<br>【定休日】毎週火曜日、第1・3月曜日</div>
  <p class="copyright">Copyright (C) Sorana All Rights Reserved.</p>
</footer>

</body>
</html>
```